Postcard Design for a Church

The postcard is for a church. This will be going to new movers in the area. I would like it to say "Welcome to the Neighborhood!" somewhere on the postcard. You can say something like like "Transitioning to a new community can be very difficult and sometimes overwhelming. Our goal as a church is to assist and help where needed". You can also say something like "if you're looking for a church home and a place where you'll be embraced, we invite you to worship with us and be our special guest". Our Facebook page is Facebook.com/TheBrightwaterHouseTN. Our Twitter is TheBrightwaterHouse. Our website page is www.TheBrightwaterHouseTN.org. You can list the vision of the church which is "Our vision is to save souls, change lives & impact the community". Please list the address of the church being located in the main auditorium of Marrowfield High School. The time is Sundays at 11am. The address is 1786 Marrowfield Lane, Dunmore, TN 37588. Our colors are purple and gold. You can also say "We're more than a church, we're a family". I would like it to also say something like "Come and Grow With Us!" My name is Pastor Desmond "LT" Fairbanks. My wife's name is First Lady Mirelle Fairbanks. I hope all this makes sense and it's not exactly in order, but I would like to see your designs. Thank you.

```html
<!DOCTYPE html>
<html lang="en">
<head>
<meta charset="utf-8">
<title>The Brightwater House – Welcome Postcard</title>
<link rel="stylesheet" href="https://fonts.googleapis.com/css2?family=Lato:wght@400;700;900&display=swap">
<style>
:root{
  --purple:#5b2682;
  --purple-deep:#47205f;
  --purple-text:#6e2f8f;
  --gold:#c9bd79;
  --ink:#1f1f1f;
  --white:#ffffff;
  --rule:#e6e6e6;
  --backdrop:#2a160c;
}
*{box-sizing:border-box;margin:0;padding:0}
html,body{width:1000px;height:1200px;overflow:hidden}
body{background:var(--backdrop);font-family:'Lato',sans-serif;position:relative}
.card{position:absolute;left:125px;width:755px;background:var(--white);overflow:hidden}
.card-front{top:15px;height:582px}
.card-back{top:609px;height:581px}
.card svg.shapes{position:absolute;left:0;top:0}
.abs{position:absolute}

.headline{left:40px;top:40px;color:var(--purple-text);font-weight:900;line-height:1}
.headline .big{font-size:40px}
.headline .small{font-size:32px;font-weight:700}
.headline .line2{display:block;text-align:right;width:390px;margin-top:6px;font-size:36px}
.intro{left:40px;top:139px;width:386px;font-size:16.8px;line-height:20.5px;color:var(--ink);text-align:justify}
.vision-mark{left:40px;top:222px;width:24px;height:24px;border-radius:50%;background:var(--gold)}
.vision{left:93px;top:213px;width:330px;font-size:16.5px;line-height:21px;color:var(--purple-text)}
.vision b{font-weight:700}
.invite{left:36px;top:269px;width:388px;font-size:16.8px;line-height:20.5px;color:var(--ink);text-align:justify}

.brand-mark{left:548px;top:28px;width:150px;height:150px;border-radius:50%;background:var(--purple);box-shadow:0 0 0 6px var(--white),0 0 0 9px var(--gold)}
.brand-name{left:520px;top:190px;width:210px;text-align:center;color:var(--purple-text);font-size:27px;font-weight:400;line-height:30px}

.details{left:42px;top:382px;color:var(--white);font-size:16.5px;line-height:22px}
.details b{font-weight:700}
.details small{font-size:14px}
.details .time{margin-top:5px}
.cta{left:40px;top:488px;color:var(--gold);font-size:30px;font-weight:900;letter-spacing:.2px}
.pastors{left:40px;top:529px;color:var(--white);font-size:16px}

.family{left:30px;top:42px;color:var(--gold);font-weight:700;line-height:1.3}
.family .l1{font-size:24px}
.family .l2{font-size:27px}
.dots{left:25px;width:300px;border-top:3px dotted var(--gold)}
.social{left:28px;color:var(--white);font-size:14.5px;display:flex;align-items:center;gap:10px}
.social i{width:18px;height:18px;border-radius:50%;background:var(--white);display:inline-block}
.site{left:28px;top:324px;color:var(--gold);font-size:15px}
.stamp{left:592px;top:30px;width:136px;height:138px;border:5px solid var(--rule)}
.addr-line{left:405px;width:323px;border-top:4px solid var(--rule)}
.back-mark{left:18px;top:456px;width:66px;height:66px;border-radius:50%;background:var(--purple);box-shadow:0 0 0 3px var(--white),0 0 0 5px var(--gold)}
.back-name{left:8px;top:528px;width:100px;text-align:center;color:var(--purple-text);font-size:14px;line-height:15px}
</style>
</head>
<body>

<section class="card card-front">
  <svg class="shapes" width="755" height="582" viewBox="0 0 755 582">
    <defs>
      <linearGradient id="portraitTone" x1="0" y1="0" x2="1" y2="1">
        <stop offset="0" stop-color="#d9d2cc"/>
        <stop offset=".5" stop-color="#7a5543"/>
        <stop offset="1" stop-color="#1b1b1b"/>
      </linearGradient>
    </defs>
    <rect x="530" y="268" width="225" height="314" fill="url(#portraitTone)" role="img" aria-label="Photo of Pastor Desmond Fairbanks and First Lady Mirelle Fairbanks"/>
    <path d="M0,366 C150,350 330,360 468,392 C500,500 600,560 755,590 L0,590 Z" fill="var(--purple)"/>
    <path d="M0,366 C150,350 330,360 468,392" fill="none" stroke="var(--gold)" stroke-width="4"/>
    <path d="M520,-5 C440,250 480,500 755,578 L755,590 C470,520 425,260 506,-5 Z" fill="var(--gold)"/>
    <path d="M525,-5 C450,250 490,495 755,572" fill="none" stroke="var(--purple-deep)" stroke-width="4"/>
  </svg>

  <h1 class="abs headline"><span class="big">WELCOME</span> <span class="small">TO THE</span><span class="line2">NEIGHBORHOOD!</span></h1>
  <p class="abs intro">Transitioning to a new community can be very difficult and sometimes overwhelming. Our goal as a church is to assist and help where needed.</p>
  <span class="abs vision-mark"></span>
  <p class="abs vision">Our vision is to <b>save souls, change lives, impact the community</b></p>
  <p class="abs invite">If you're looking for a church home and a place where you'll be embraced, we invite you to worship with us and be our special guest.</p>

  <span class="abs brand-mark"></span>
  <p class="abs brand-name">The Brightwater House</p>

  <div class="abs details">
    <p>Address:</p>
    <p><b>Marrowfield High School</b> <small>(main auditorium)</small></p>
    <p>1786 Marrowfield Lane, Dunmore, TN 37588</p>
    <p class="time"><b>Sundays</b> at <b>11 am</b></p>
  </div>
  <p class="abs cta">COME AND GROW WITH US!</p>
  <p class="abs pastors">Pastor Desmond "LT" Fairbanks &amp; wife Lady Mirelle Fairbanks</p>
</section>

<section class="card card-back">
  <svg class="shapes" width="755" height="581" viewBox="0 0 755 581">
    <path d="M0,470 C150,470 330,380 365,150" fill="none" stroke="#efefef" stroke-width="14"/>
    <path d="M0,500 C170,500 350,400 372,200" fill="none" stroke="#f3f3f3" stroke-width="12"/>
    <path d="M0,530 C190,530 360,430 375,260" fill="none" stroke="#f6f6f6" stroke-width="10"/>
    <circle cx="110" cy="186" r="254" fill="var(--gold)"/>
    <circle cx="108" cy="184" r="250" fill="var(--purple-deep)"/>
  </svg>

  <h2 class="abs family"><span class="l1">WE'RE MORE THAN</span><br><span class="l2">A CHURCH,</span><br><span class="l2">WE'RE A FAMILY</span></h2>
  <span class="abs dots" style="top:175px"></span>
  <p class="abs social" style="top:210px"><i></i>www.gatherly.com/TheBrightwaterHouseTN</p>
  <p class="abs social" style="top:244px"><i></i>www.chirpline.com/TheBrightwaterHouse</p>
  <span class="abs dots" style="top:297px"></span>
  <p class="abs site">www.TheBrightwaterHouseTN.org</p>

  <span class="abs stamp"></span>
  <span class="abs addr-line" style="top:274px"></span>
  <span class="abs addr-line" style="top:336px"></span>
  <span class="abs addr-line" style="top:397px"></span>
  <span class="abs addr-line" style="top:467px"></span>

  <span class="abs back-mark"></span>
  <p class="abs back-name">The Brightwater House</p>
</section>

</body>
</html>
```